Create a pouch design for a new sports supplement product

Dimensions are 235mm (width) x 335mm (length) x 110mm (gusset)
File 1 - Extension of design brief please read both briefs
File 2 - Is 2 potential pouches this is just to give you a better example of size the dimensions are for the pouch on the right. This picture is not to give you design ideas as I am not very keen on either of these designs.
We need a design to be printed onto the pouches of our whey protein product. The brand name is 'Stellar Fuelworks' and needs to be displayed on the packaging either just writing or a simple logo design. I am not the most creative person in the world but have put together a more detailed brief listing some of the key information that needs to be included on the pouch (See attachment) Please feel free if you have experience of this the sports supplement market or have different ideas then please feel free to explore them.
The pouch would either be printed straight onto the pouch, or possibly just a printed label (front & back) to be stuck onto the pouch. Please design either or both.
Open to different colour schemes. Design has to be modern looking and eye-catching.
Some key points;
High quality whey protein concentrate
All Natural
Soy free
Great tasting
Please google image search 'protein pouches' to see other designs if your not familiar with the sports supplement market.
Any questions feel free to ask.
Updates
Hi, Thanks for all your design! I am really busy at the moment so haven't had chance to give feedback and have a proper look through all the designs. I have extended the time frame to give myself chance to give proper feedback and see any changes needed. Expect feedback sunday at the latest, and I will be pick a design early next week.
Target Market(s)
Sports supplement market. Product is a whey protein shake
Industry/Entity Type
Nutrition
Look and feel
Each slider illustrates characteristics of the customer's brand and the style your logo design should communicate.

```html
<!DOCTYPE html>
<html lang="en">
<head>
<meta charset="utf-8">
<title>Stellar Fuelworks Whey Protein Pouch</title>
<link href="https://fonts.googleapis.com/css2?family=Anton&family=Montserrat:wght@300;400;600;700&display=swap" rel="stylesheet">
<style>
  :root {
    --backdrop: #7b726b;
    --lime: #d3e227;
    --ink: #141414;
    --pouch-black: #1b1b1b;
    --white: #f2f2f2;
    --muted: #bdbdbd;
    --display: "Anton", "Impact", sans-serif;
    --body: "Montserrat", "Helvetica Neue", sans-serif;
  }
  * { box-sizing: border-box; margin: 0; padding: 0; }
  html, body { width: 1200px; height: 849px; overflow: hidden; }
  body { background: var(--backdrop); position: relative; font-family: var(--body); }

  .pouch { position: absolute; top: 185px; width: 340px; height: 508px; overflow: hidden; border-radius: 4px; }
  .tear-line { position: absolute; left: 0; right: 0; top: 30px; border-top: 1px dashed rgba(0,0,0,.45); }

  /* Front */
  .pouch--front { left: 208px; background: var(--lime); }
  .front-band { position: absolute; left: 54px; top: 0; width: 213px; height: 82px; background: var(--ink); }
  .tear-label { position: absolute; right: 14px; top: 18px; font-size: 6px; letter-spacing: .5px; color: #333; }
  .tear-mark { position: absolute; left: 14px; top: 22px; font-size: 9px; color: #333; }
  .brand-front { position: absolute; left: 54px; top: 86px; width: 260px; font-family: var(--display); color: var(--ink); font-size: 38px; line-height: 37px; text-transform: uppercase; }
  .headline { position: absolute; left: 16px; top: 164px; font-family: var(--display); color: var(--ink); text-transform: uppercase; font-weight: 400; }
  .headline span { display: block; white-space: nowrap; }
  .headline .line-1 { font-size: 40px; line-height: 40px; }
  .headline .line-2 { font-size: 104px; line-height: 100px; letter-spacing: 6px; }
  .headline .line-3 { font-size: 88px; line-height: 88px; letter-spacing: 3px; }
  .front-claims { position: absolute; right: 28px; top: 400px; text-align: right; font-weight: 300; font-size: 15px; line-height: 20px; color: var(--ink); text-transform: uppercase; }

  /* Back */
  .pouch--back { left: 600px; background: var(--pouch-black); color: var(--white); }
  .pouch--back .tear-line { border-color: rgba(255,255,255,.35); }
  .back-block { position: absolute; left: 0; top: 0; width: 112px; height: 96px; background: var(--lime); }
  .brand-back { position: absolute; left: 20px; top: 52px; font-family: var(--display); font-size: 19px; line-height: 19px; color: var(--ink); text-transform: uppercase; }
  .back-title { position: absolute; right: 44px; top: 44px; font-family: var(--display); font-weight: 400; color: var(--lime); text-transform: uppercase; text-align: center; }
  .back-title span { display: block; }
  .back-title .small { font-size: 12px; line-height: 13px; }
  .back-title .big { font-size: 22px; line-height: 22px; }
  .intro { position: absolute; left: 30px; right: 26px; top: 106px; font-size: 7px; font-weight: 700; line-height: 9.6px; }
  .benefits { position: absolute; left: 30px; right: 26px; top: 162px; list-style: none; }
  .benefits li { font-size: 7px; line-height: 9px; margin-bottom: 7px; padding-left: 10px; position: relative; }
  .benefits li::before { content: "•"; position: absolute; left: 0; }
  .benefits strong { display: block; font-weight: 700; text-transform: uppercase; }
  .benefits span { color: var(--muted); font-weight: 400; }

  .nutrition { position: absolute; left: 28px; top: 248px; width: 114px; background: var(--white); color: var(--ink); padding: 3px 4px; font-size: 4.6px; line-height: 6px; }
  .nutrition h3 { font-family: var(--body); font-weight: 700; font-size: 10px; line-height: 11px; border-bottom: 2px solid var(--ink); }
  .nutrition table { width: 100%; border-collapse: collapse; }
  .nutrition td { border-bottom: .5px solid #555; padding: .3px 0; }
  .nutrition td:last-child { text-align: right; }
  .nutrition .bold td:first-child { font-weight: 700; }
  .nutrition .rule td { border-bottom: 2px solid var(--ink); }
  .nutrition p { margin-top: 2px; }

  .details { position: absolute; left: 156px; right: 24px; top: 248px; font-size: 6.2px; line-height: 8.2px; color: var(--muted); }
  .details p { margin-bottom: 7px; }
  .details strong { color: var(--white); font-weight: 700; }
  .connect { position: absolute; left: 156px; top: 418px; font-size: 8px; font-weight: 700; line-height: 11px; }
  .social { position: absolute; left: 246px; top: 420px; display: flex; gap: 5px; }
  .social span { width: 13px; height: 13px; background: var(--white); display: block; }
</style>
</head>
<body>

<section class="pouch pouch--front" aria-label="Front of pouch">
  <div class="front-band"></div>
  <span class="tear-mark">✂</span>
  <span class="tear-label">TEAR &amp; RESEAL</span>
  <div class="tear-line"></div>
  <div class="brand-front">Stellar<br>Fuelworks</div>
  <h1 class="headline">
    <span class="line-1">High Quality</span>
    <span class="line-2">Whey</span>
    <span class="line-3">Protein</span>
  </h1>
  <p class="front-claims">No artificial flavours<br>Excellent amino acid profile</p>
</section>

<section class="pouch pouch--back" aria-label="Back of pouch">
  <div class="back-block"></div>
  <div class="tear-line"></div>
  <div class="brand-back">Stellar<br>Fuelworks</div>
  <h2 class="back-title"><span class="small">High Quality</span><span class="big">Whey</span><span class="big">Protein</span></h2>

  <p class="intro">Stellar Fuelworks' natural whey protein is a very high quality 100% natural instant whey protein concentrate impressively providing 80% protein content making this the perfect supplement to aid muscular growth and repair. In addition this all the ingredients are natural but yet still providing a great taste which will make you want more.</p>

  <ul class="benefits">
    <li><strong>Build, repair and grow</strong><span>High protein content to maximise strength muscular strength and size gains</span></li>
    <li><strong>Excellent amino acid profile</strong><span>High quality whey protein concentrate with high levels of essential and non essential amino acids vital to muscular repair.</span></li>
    <li><strong>No artificial flavours</strong><span>Only the best natural and great taste flavours used</span></li>
  </ul>

  <div class="nutrition">
    <h3>Nutrition Facts</h3>
    <table>
      <tr><td>Serving Size 25g</td><td></td></tr>
      <tr class="rule"><td>Servings Per Pack 40</td><td></td></tr>
      <tr class="bold"><td>Calories 100</td><td>% Daily Value</td></tr>
      <tr class="bold"><td>Total Fat 2g</td><td>3%</td></tr>
      <tr><td>Saturated Fat 1g</td><td>5%</td></tr>
      <tr><td>Trans Fat 0g</td><td>0%</td></tr>
      <tr class="bold"><td>Cholesterol 15mg</td><td>5%</td></tr>
      <tr class="bold"><td>Sodium 50mg</td><td>2%</td></tr>
      <tr class="bold"><td>Potassium 120mg</td><td>3%</td></tr>
      <tr class="bold"><td>Total Carbohydrate 2g</td><td>1%</td></tr>
      <tr><td>Dietary Fiber 0g</td><td>0%</td></tr>
      <tr><td>Sugars 2g</td><td></td></tr>
      <tr class="bold rule"><td>Protein 20g</td><td>40%</td></tr>
      <tr><td>Vitamin A 0% · Vitamin C 0%</td><td></td></tr>
      <tr><td>Calcium 8% · Iron 0%</td><td></td></tr>
    </table>
    <p>* Percent Daily Values are based on a 2,000 calorie diet. Your values may be higher or lower depending on your calorie needs.</p>
  </div>

  <div class="details">
    <p><strong>Ingredients;</strong><br>Whey protein concentrate 80%, Flavouring, sweetener, colour, sunflower lecithin.</p>
    <p><strong>Storage</strong> – Store in a cool dry place</p>
    <p><strong>Serving suggestions</strong> – Mix 25g with 150-250ml of water or milk, consume 1-4 times daily and ideally straight after working out. The less liquid, the thicker the shake.</p>
    <p>Do not exceed serving suggestion, and always consult a doctor before use.</p>
    <p>Natural whey protein should be consumed alongside a well balanced healthy diet and training programme.</p>
    <p>For any enquiries to see website:<br>UK manufactured, Stellar Fuelworks, unit 4, Orbit Court, Northfield, NF12 3AB, UK</p>
  </div>

  <p class="connect">Connect with us:<br>Stellar-Fuelworks.eu</p>
  <div class="social" aria-hidden="true"><span></span><span></span><span></span></div>
</section>

</body>
</html>
```